Company presentation powerpoint template

Hello,
We are a cloud computing solution who focus to provide complete cloud solution for enterprise. We need a PPT template to introduce our company and solution. Our website is http://www.lumaversa.com, it would be great if the design will match our website style.
Industry/Entity Type
It Company

```html
<!DOCTYPE html>
<html lang="en">
<head>
<meta charset="utf-8">
<title>Table – Financial Data</title>
<link rel="stylesheet" href="https://fonts.googleapis.com/css2?family=Jost:wght@400;500&family=Roboto:wght@400;700&display=swap">
<style>
  :root {
    --ink-title: #3d5a6e;
    --accent-line: #5fc4ec;
    --brand-blue: #1ba1dc;
    --header-bg: #2586b9;
    --label-strong: #b9e1f1;
    --label-soft: #d8eef6;
    --cell-white: #ffffff;
    --cell-grey: #e1e1e1;
    --cell-text: #6a6a6a;
    --footer-blue: #0b97d9;
    --footer-deep: #0a7fbd;
    --white: #ffffff;
  }
  * { box-sizing: border-box; margin: 0; padding: 0; }
  html, body { width: 1200px; height: 900px; overflow: hidden; background: var(--white); }
  .slide { position: relative; width: 1200px; height: 900px; background: var(--white); font-family: "Roboto", Arial, sans-serif; }

  .slide-title {
    position: absolute; left: 46px; top: 28px;
    font-family: "Jost", "Futura", sans-serif; font-weight: 400;
    font-size: 36px; letter-spacing: 1px; color: var(--ink-title);
  }
  .title-rule {
    position: absolute; left: 0; top: 89px; width: 1010px; height: 4px;
    background: var(--accent-line);
  }
  .brand {
    position: absolute; right: 46px; top: 58px;
    display: flex; align-items: center; gap: 10px;
    font-family: "Roboto", Arial, sans-serif; font-weight: 700;
    font-size: 30px; color: var(--brand-blue);
  }
  .brand-dot { width: 16px; height: 16px; border-radius: 50%; background: var(--brand-blue); }

  .finance-table {
    position: absolute; left: 52px; top: 172px; width: 1087px;
    border-collapse: collapse; table-layout: fixed;
    border-bottom: 2px solid var(--accent-line);
  }
  .finance-table col.label-col { width: 278px; }
  .finance-table th {
    height: 81px; background: var(--header-bg); color: var(--white);
    font-weight: 700; font-size: 24px; text-align: center;
    text-shadow: 0 1px 2px rgba(0,0,0,0.25);
  }
  .finance-table th.label-head { text-align: left; padding-left: 36px; font-size: 28px; }
  .finance-table td {
    height: 70.5px; text-align: center; font-size: 21px; color: var(--cell-text);
    background: var(--cell-white);
  }
  .finance-table td.row-label {
    text-align: left; padding-left: 36px; font-size: 24px;
    background: var(--label-strong);
  }
  .finance-table tbody tr:nth-child(even) td { background: var(--cell-grey); }
  .finance-table tbody tr:nth-child(even) td.row-label { background: var(--label-soft); }

  .footer-band {
    position: absolute; left: 0; top: 852px; width: 1200px; height: 38px;
    background: var(--footer-blue);
  }
  .footer-strip {
    position: absolute; left: 0; top: 890px; width: 1200px; height: 10px;
    background: var(--footer-deep);
  }
  .footer-url {
    position: absolute; left: 18px; top: 861px;
    font-size: 19px; color: var(--white);
  }
  .page-number {
    position: absolute; left: 1111px; top: 854px;
    font-size: 17px; color: var(--white);
  }
</style>
</head>
<body>
<div class="slide">
  <h1 class="slide-title">TABLE – FINANCIAL DATA</h1>
  <div class="title-rule"></div>
  <div class="brand"><span class="brand-dot"></span>Lumaversa</div>

  <table class="finance-table">
    <colgroup>
      <col class="label-col"><col><col><col><col><col>
    </colgroup>
    <thead>
      <tr>
        <th class="label-head">Lorem</th>
        <th>Year 1</th><th>Year 2</th><th>Year 3</th><th>Year 4</th><th>Year 5</th>
      </tr>
    </thead>
    <tbody>
      <tr><td class="row-label">Lorem</td><td>Lorem</td><td>Lorem</td><td>Lorem</td><td>Lorem</td><td>Lorem</td></tr>
      <tr><td class="row-label">Lorem</td><td>Lorem</td><td>Lorem</td><td>Lorem</td><td>Lorem</td><td>Lorem</td></tr>
      <tr><td class="row-label">Lorem</td><td>Lorem</td><td>Lorem</td><td>Lorem</td><td>Lorem</td><td>Lorem</td></tr>
      <tr><td class="row-label">Lorem</td><td>Lorem</td><td>Lorem</td><td>Lorem</td><td>Lorem</td><td>Lorem</td></tr>
      <tr><td class="row-label">Lorem</td><td>Lorem</td><td>Lorem</td><td>Lorem</td><td>Lorem</td><td>Lorem</td></tr>
      <tr><td class="row-label">Lorem</td><td>Lorem</td><td>Lorem</td><td>Lorem</td><td>Lorem</td><td>Lorem</td></tr>
      <tr><td class="row-label">Lorem</td><td>Lorem</td><td>Lorem</td><td>Lorem</td><td>Lorem</td><td>Lorem</td></tr>
    </tbody>
  </table>

  <div class="footer-band"></div>
  <div class="footer-strip"></div>
  <div class="footer-url">www.lumaversa.com</div>
  <div class="page-number">3</div>
</div>
</body>
</html>
```